Service Plans and Offerings - One Page

We are looking for an 8.5 x 11 one page in a portrait orientation that advertises our product and service offerings on one side and our logo and a slogan, "Reliable Managed IT Services & Support" - "TALMERO is ready to earn your trust" on the other with TALMERO contact information.

This brochure would be left at prospect client's business, so it needs to be inviting, professional, and clear.

Attached is one excel sheet with 4 columns representing our Service Plans and Offerings (Ideas on the descriptive names for the different service offering level is welcome) that we would like you to use for inspiration for the written content in the handout.

The brochure should have the TALMERO contact information on the bottom of the services description page and on the other side of the page (not necessary located at bottom). TALMERO contact information (email, phone, website) will provided to contest winner.

Please be creative with both the content and the design.

Target Market(s)

Small to medium companies with 5-50 seats.

Industry/Entity Type

Information Technology (IT) Managed Service Provider

Font styles to use
Serif

Colors
0094D4
00A9DD
6FCCEA
C7EBF8
E9F6FB

Requirements
Must have
• Clear and professional representation of TALMERO Product Services Plans and easy to read TALMERO contact information.

```html
<!DOCTYPE html>
<html lang="en">
<head>
<meta charset="utf-8">
<title>TALMERO – Reliable Managed IT Services &amp; Support</title>
<link href="https://fonts.googleapis.com/css2?family=Poppins:wght@400;500;600;700&display=swap" rel="stylesheet">
<style>
  :root{
    --navy:#0a3553;
    --navy-dark:#072638;
    --blue:#1b8fc6;
    --blue-bright:#0094d4;
    --tag-blue:#1b7fb8;
    --sky:#6fccea;
    --card-top:#9fd6ef;
    --card-bottom:#6fbde4;
    --pale:#e9f6fb;
    --ice:#c7ebf8;
    --cell:#e8e9eb;
    --cell-alt:#d9dbde;
    --check:#1f8a3a;
    --canvas:#e4e4e4;
    --ink:#1f2b36;
  }
  *{box-sizing:border-box;margin:0;padding:0}
  html,body{width:884px;height:1200px;overflow:hidden;background:var(--canvas)}
  body{position:relative;font-family:"Poppins",sans-serif;color:var(--ink)}

  .sheet-slot{position:absolute;left:212px;width:460px;height:593px;overflow:hidden;
    box-shadow:0 2px 8px rgba(0,0,0,.25);background:#fff}
  .sheet-slot.front{top:4px}
  .sheet-slot.back{top:603px}
  .sheet{position:absolute;left:0;top:0;width:884px;height:1140px;overflow:hidden;
    transform:scale(.52);transform-origin:0 0;
    background:linear-gradient(180deg,#f4fafd 0%,var(--pale) 60%,#f7fbfd 100%)}

  /* shared hero */
  .hero{position:absolute;left:0;top:0;width:884px;height:318px;
    background:linear-gradient(100deg,#07182a 0%,#0d2a40 38%,#4a3424 62%,#6b4a30 80%,#3a2a20 100%)}
  .hero-shade{position:absolute;left:0;top:0;width:560px;height:318px;
    background:linear-gradient(90deg,rgba(5,20,35,.92) 0%,rgba(5,20,35,.7) 70%,rgba(5,20,35,0) 100%)}
  .brand{position:absolute;left:52px;top:58px;display:flex;align-items:center;gap:12px}
  .brand-dot{width:34px;height:34px;border-radius:50%;background:var(--blue-bright)}
  .brand-name{font-size:36px;font-weight:600;color:var(--blue-bright);letter-spacing:3px}
  .hero-rule{position:absolute;left:52px;width:380px;height:2px;background:#fff}
  .hero-rule::before{content:"";position:absolute;left:0;top:-4px;width:9px;height:9px;border:2px solid #fff}

  /* front */
  .headline{position:absolute;left:52px;top:150px;line-height:1}
  .headline .l1{display:block;font-size:37px;font-weight:600;color:#fff;letter-spacing:.5px}
  .headline .l2{display:block;font-size:31px;font-weight:600;color:var(--blue-bright);margin-top:2px}
  .front .hero-rule{top:232px}
  .tagline{position:absolute;left:52px;top:248px;font-size:15px;color:#fff;font-weight:500}
  .band{position:absolute;left:0;top:300px}

  .section-title{position:absolute;left:52px;top:352px;display:flex;align-items:center;gap:10px}
  .section-bar{width:7px;height:46px;background:var(--blue-bright)}
  .section-pill{background:var(--navy);color:#fff;font-size:21px;font-weight:500;
    padding:8px 26px 8px 18px;border-radius:0 24px 24px 0}
  .intro{position:absolute;left:52px;top:414px;width:780px;font-size:12.3px;line-height:1.38;color:#222}
  .intro b{color:var(--navy)}

  .service{position:absolute;left:60px;width:760px;height:118px}
  .service-card{position:absolute;left:44px;top:0;width:716px;height:118px;border-radius:18px;
    background:linear-gradient(180deg,var(--card-top),var(--card-bottom));
    border:2px solid #5db0dc;padding:6px 24px 0 90px}
  .service-card h3{font-size:18px;font-weight:500;color:#fff;text-decoration:underline;text-underline-offset:4px;
    text-decoration-thickness:1px;margin-bottom:6px;letter-spacing:.3px}
  .service-card p{font-size:11px;line-height:1.38;color:#1a2733}
  .service-icon{position:absolute;left:0;top:1px;width:116px;height:116px;border-radius:50%;
    background:#fff;box-shadow:0 3px 8px rgba(0,0,0,.25);display:flex;align-items:center;justify-content:center}
  .service-icon .disc{width:96px;height:96px;border-radius:50%;background:var(--navy);display:flex;align-items:center;justify-content:center}

  .footer{position:absolute;left:0;top:1010px;width:884px;height:130px}
  .footer-band{position:absolute;left:0;top:20px;width:884px;height:110px;
    background:linear-gradient(90deg,var(--blue) 0%,#2a9fd6 60%,var(--blue) 100%)}
  .contact-block{position:absolute;left:0;top:0}
  .contact-label{position:absolute;left:52px;top:60px;font-size:22px;font-weight:600;color:#fff;letter-spacing:.5px}
  .contact-item{position:absolute;top:64px;display:flex;align-items:center;gap:10px;color:#fff;font-size:15px;font-weight:500}
  .contact-item.small{font-size:13px;line-height:1.2;top:58px}
  .contact-item.web{top:64px}
  .contact-icon{width:20px;height:20px;flex:none}

  /* back */
  .back .sheet{background:#fff}
  .back .hero{height:200px}
  .back .hero-shade{height:200px}
  .back .brand{top:40px}
  .plans-title{position:absolute;left:52px;top:100px;font-size:36px;font-weight:600;color:#fff;letter-spacing:.5px;line-height:1}
  .plans-title span{color:var(--blue-bright)}
  .back .hero-rule{top:150px;width:400px}
  .back-band{position:absolute;left:0;top:194px;width:884px;height:18px;background:var(--blue)}
  .back-foot{position:absolute;left:0;top:1112px;width:884px;height:28px;
    background:linear-gradient(90deg,var(--blue),#2a9fd6,var(--blue))}

  .plans{position:absolute;left:82px;top:231px;width:714px}
  .plan-grid{display:grid;grid-template-columns:170px 143px 119px 119px 130px;column-gap:8px}
  .tier{display:flex;flex-direction:column;align-items:center}
  .tier-name{width:100%;height:22px;background:var(--navy);color:#fff;font-size:11.5px;font-weight:500;
    text-align:center;line-height:22px;border-radius:3px 3px 0 0}
  .tier-num{width:14px;height:14px;border-radius:50%;background:#fff;color:var(--navy);font-size:8px;font-weight:600;
    text-align:center;line-height:14px;margin:-2px 0 -2px;position:relative;z-index:1}
  .tier-metal{width:100%;height:18px;font-size:11px;font-weight:600;text-align:center;line-height:18px}
  .bronze{background:linear-gradient(90deg,#7e5226,#c08a4a,#7e5226);color:#fff}
  .silver{background:linear-gradient(90deg,#b3b8be,#e3e6e9,#b3b8be);color:#1f2b36}
  .gold{background:linear-gradient(90deg,#b8901c,#f0d060,#b8901c);color:#fff}
  .platinum{background:linear-gradient(90deg,#8e959d,#d6dade,#8e959d);color:#1f2b36}

  .plan-group{margin-top:10px}
  .group-tag{width:170px;height:15px;background:var(--tag-blue);color:#fff;font-size:10.5px;font-weight:600;
    line-height:15px;padding-left:8px;border-radius:3px 3px 0 0;letter-spacing:.3px}
  .plan-row .feature{display:flex;align-items:center;min-height:22px;padding:2px 8px;font-size:11.5px;font-weight:500;
    line-height:1.05;background:#f2f3f4}
  .plan-row .cell{display:flex;align-items:center;justify-content:center;background:var(--cell)}
  .plan-row.tall .feature{min-height:30px}
  .plan-group .plan-row:nth-of-type(odd) .cell{background:var(--cell-alt)}
  .plan-group .plan-row:nth-of-type(odd) .feature{background:#e8eaec}
  .check{display:inline-block;width:12px;height:12px;border-radius:50%;background:var(--check);position:relative}
  .check::after{content:"";position:absolute;left:4px;top:2px;width:3px;height:6px;border:solid #fff;
    border-width:0 1.6px 1.6px 0;transform:rotate(45deg)}
  .price-row{margin-top:10px}
  .price{height:17px;background:var(--navy);color:#fff;font-size:11px;font-weight:500;text-align:center;line-height:17px}
  .price sup{font-size:7px;vertical-align:4px}
</style>
</head>
<body>

<!-- Front side -->
<div class="sheet-slot front">
<main class="sheet">
  <header>
    <div class="hero" role="img" aria-label="Overhead photo of a business team joining hands over a wooden meeting table with laptops and coffee cups"></div>
    <div class="hero-shade"></div>
    <div class="brand"><span class="brand-dot"></span><span class="brand-name">TALMERO</span></div>
    <h1 class="headline"><span class="l1">RELIABLE MANAGED</span><span class="l2">IT SERVICES &amp; SUPPORT</span></h1>
    <div class="hero-rule"></div>
    <p class="tagline">TALMERO IS READY TO EARN YOUR TRUST</p>
    <svg class="band" width="884" height="40" viewBox="0 0 884 40">
      <polygon points="0,18 884,0 884,10 0,40" fill="#1b8fc6"/>
      <polygon points="0,40 884,10 884,40" fill="#e9f6fb"/>
    </svg>
  </header>

  <div class="section-title"><span class="section-bar"></span><h2 class="section-pill">IT SOLUTIONS</h2></div>
  <p class="intro"><b>TALMERO</b> has been providing IT Solutions to the Alberta, and BC market since 2014. We have earned our client's trust through providing IT Solutions that work and add value to their companies. With our comprehensive service approach, we make the complex simple.</p>

  <section class="service" style="top:488px">
    <div class="service-card">
      <h3>MANAGED IT SERVICES</h3>
      <p>The IT function is an essential part of any business committed to being efficient, relevant and effective in today's overly competitive market. IT has evolved over the years. However, small and medium-sized companies and organizations lack the necessary resources to employ talented resources to manage their IT needs. To remain competitive and have confidence in your technology investment health, TALMERO is ready to earn your trust as its Managed IT Partner.</p>
    </div>
    <div class="service-icon"><div class="disc">
      <svg width="52" height="52" viewBox="0 0 54 54" fill="none" stroke="#fff" stroke-width="3" stroke-linejoin="round">
        <rect x="10" y="12" width="34" height="22" rx="2"/><path d="M4 40h46l-4 5H8z" fill="#fff"/>
      </svg>
    </div></div>
  </section>

  <section class="service" style="top:618px">
    <div class="service-card">
      <h3>CLOUD SERVICES</h3>
      <p>Cloud services refer to various services delivered on request to customers and companies through the internet specially designed to offer affordable and easy access to resources and applications without the need for internal hardware or infrastructure.</p>
    </div>
    <div class="service-icon"><div class="disc">
      <svg width="54" height="54" viewBox="0 0 56 56" fill="none" stroke="#fff" stroke-width="3" stroke-linejoin="round">
        <path d="M14 26a10 10 0 0 1 4-14 12 12 0 0 1 20 2 9 9 0 0 1 6 12z" fill="#fff"/>
        <rect x="10" y="28" width="36" height="10" rx="1"/><rect x="10" y="40" width="36" height="10" rx="1"/>
        <path d="M15 33h12M15 45h12" stroke-width="2"/>
      </svg>
    </div></div>
  </section>

  <section class="service" style="top:748px">
    <div class="service-card">
      <h3>REMOTE WORK</h3>
      <p>Improving flexibility of operations during a global pandemic. Increasing employee quality of life. Decreasing company overhead. Helping the environment. Whichever of the many valid reasons relate to your situation, it's entirely clear that the office of the future—and for many, the present—is at the home.</p>
    </div>
    <div class="service-icon"><div class="disc">
      <svg width="54" height="54" viewBox="0 0 56 56" fill="none" stroke="#fff" stroke-width="3" stroke-linejoin="round">
        <path d="M6 26L28 8l22 18"/><path d="M12 22v28h32V22"/>
        <rect x="18" y="34" width="20" height="12" fill="#fff"/>
      </svg>
    </div></div>
  </section>

  <section class="service" style="top:878px">
    <div class="service-card">
      <h3>CYBER SECURITY</h3>
      <p>IT security is a collection of mature cybersecurity procedures that prevent unauthorized access to company assets like networks, computers, and data. Alberta &amp; BC Cybersecurity companies, such as TALMERO, help maintain the confidentiality and integrity of business information by blocking hackers and external threats from accessing these devices.</p>
    </div>
    <div class="service-icon"><div class="disc">
      <svg width="54" height="54" viewBox="0 0 56 56" fill="none" stroke="#fff" stroke-width="3" stroke-linejoin="round">
        <path d="M28 6l18 7v12c0 12-8 20-18 24-10-4-18-12-18-24V13z"/>
        <rect x="20" y="26" width="16" height="12" fill="#fff"/><path d="M23 26v-4a5 5 0 0 1 10 0v4"/>
      </svg>
    </div></div>
  </section>

  <footer class="footer">
    <div class="footer-band"></div>
    <svg class="contact-block" width="260" height="130" viewBox="0 0 260 130">
      <polygon points="0,0 246,0 232,130 0,130" fill="#072638"/>
    </svg>
    <h2 class="contact-label">CONTACT US</h2>
    <div class="contact-item" style="left:262px">
      <svg class="contact-icon" viewBox="0 0 20 20"><rect x="1" y="1" width="18" height="18" rx="3" fill="none" stroke="#fff" stroke-width="1.6"/><path d="M6 5l2 0 1 3-1.5 1a7 7 0 0 0 3.5 3.5l1-1.5 3 1 0 2c-5 .5-9.5-4-9-9z" fill="#fff"/></svg>
      <span>403-555-0182</span>
    </div>
    <div class="contact-item small" style="left:452px">
      <svg class="contact-icon" viewBox="0 0 20 20"><rect x="1" y="1" width="18" height="18" rx="3" fill="none" stroke="#fff" stroke-width="1.6"/><path d="M10 4a4 4 0 0 0-4 4c0 3 4 8 4 8s4-5 4-8a4 4 0 0 0-4-4z" fill="#fff"/><circle cx="10" cy="8" r="1.5" fill="#1b8fc6"/></svg>
      <span>118 Prairie Ave, Red Creek,<br>AB T0M 0X0</span>
    </div>
    <div class="contact-item small web" style="left:690px">
      <svg class="contact-icon" viewBox="0 0 20 20"><rect x="1" y="1" width="18" height="18" rx="3" fill="none" stroke="#fff" stroke-width="1.6"/><circle cx="10" cy="10" r="5" fill="none" stroke="#fff" stroke-width="1.4"/><path d="M5 10h10M10 5c-2 3-2 7 0 10M10 5c2 3 2 7 0 10" stroke="#fff" stroke-width="1.1" fill="none"/></svg>
      <span>www.talmero.com</span>
    </div>
  </footer>
</main>
</div>

<!-- Back side -->
<div class="sheet-slot back">
<main class="sheet">
  <header>
    <div class="hero" role="img" aria-label="Overhead photo of a business team joining hands over a wooden meeting table"></div>
    <div class="hero-shade"></div>
    <div class="brand"><span class="brand-dot"></span><span class="brand-name">TALMERO</span></div>
    <h1 class="plans-title">OUR SERVICE <span>PLANS</span></h1>
    <div class="hero-rule"></div>
    <div class="back-band"></div>
  </header>

  <section class="plans">
    <div class="plan-grid plan-head">
      <div></div>
      <div class="tier"><div class="tier-name">ECONOMIC TRUST</div><div class="tier-num">1</div><div class="tier-metal bronze">BRONZE</div></div>
      <div class="tier"><div class="tier-name">MIDDLE TRUST</div><div class="tier-num">2</div><div class="tier-metal silver">SILVER</div></div>
      <div class="tier"><div class="tier-name">HIGH TRUST</div><div class="tier-num">3</div><div class="tier-metal gold">GOLD</div></div>
      <div class="tier"><div class="tier-name">COMPLETE TRUST</div><div class="tier-num">4</div><div class="tier-metal platinum">PLATINUM</div></div>
    </div>

    <div class="plan-group">
      <div class="group-tag">FORTIFY</div>
      <div class="plan-grid plan-row"><div class="feature">Managed Firewall</div><div class="cell"></div><div class="cell"></div><div class="cell"><span class="check"></span></div><div class="cell"><span class="check"></span></div></div>
      <div class="plan-grid plan-row tall"><div class="feature">AI-Based Next Gen Anti-Virus</div><div class="cell"></div><div class="cell"></div><div class="cell"><span class="check"></span></div><div class="cell"><span class="check"></span></div></div>
      <div class="plan-grid plan-row"><div class="feature">Traditional AV</div><div class="cell"><span class="check"></span></div><div class="cell"><span class="check"></span></div><div class="cell"></div><div class="cell"></div></div>
      <div class="plan-grid plan-row tall"><div class="feature">24/7 Security Operations Centre</div><div class="cell"></div><div class="cell"></div><div class="cell"><span class="check"></span></div><div class="cell"><span class="check"></span></div></div>
    </div>

    <div class="plan-group">
      <div class="group-tag">FOUNDATION</div>
      <div class="plan-grid plan-row"><div class="feature">24/7 Monitoring</div><div class="cell"><span class="check"></span></div><div class="cell"><span class="check"></span></div><div class="cell"><span class="check"></span></div><div class="cell"><span class="check"></span></div></div>
      <div class="plan-grid plan-row"><div class="feature">Security Patching</div><div class="cell"><span class="check"></span></div><div class="cell"><span class="check"></span></div><div class="cell"><span class="check"></span></div><div class="cell"><span class="check"></span></div></div>
      <div class="plan-grid plan-row"><div class="feature">Application Updates</div><div class="cell"><span class="check"></span></div><div class="cell"><span class="check"></span></div><div class="cell"><span class="check"></span></div><div class="cell"><span class="check"></span></div></div>
      <div class="plan-grid plan-row tall"><div class="feature">Pro-active Maintenance</div><div class="cell"><span class="check"></span></div><div class="cell"><span class="check"></span></div><div class="cell"><span class="check"></span></div><div class="cell"><span class="check"></span></div></div>
    </div>

    <div class="plan-group">
      <div class="group-tag">BACKUPS</div>
      <div class="plan-grid plan-row"><div class="feature">Offsite Backups</div><div class="cell"></div><div class="cell"></div><div class="cell"></div><div class="cell"><span class="check"></span></div></div>
      <div class="plan-grid plan-row"><div class="feature">Email Backups</div><div class="cell"></div><div class="cell"></div><div class="cell"></div><div class="cell"><span class="check"></span></div></div>
      <div class="plan-grid plan-row"><div class="feature">Onsite Backups</div><div class="cell"></div><div class="cell"><span class="check"></span></div><div class="cell"><span class="check"></span></div><div class="cell"><span class="check"></span></div></div>
    </div>

    <div class="plan-group">
      <div class="group-tag">VIGILENCE</div>
      <div class="plan-grid plan-row"><div class="feature">Dark Web Monitoring</div><div class="cell"></div><div class="cell"></div><div class="cell"><span class="check"></span></div><div class="cell"><span class="check"></span></div></div>
      <div class="plan-grid plan-row"><div class="feature">Annual User Training</div><div class="cell"></div><div class="cell"></div><div class="cell"></div><div class="cell"><span class="check"></span></div></div>
    </div>

    <div class="plan-group">
      <div class="group-tag">STRATEGY</div>
      <div class="plan-grid plan-row"><div class="feature">IT Strategic Planning</div><div class="cell"></div><div class="cell"></div><div class="cell"></div><div class="cell"><span class="check"></span></div></div>
      <div class="plan-grid plan-row"><div class="feature">Technology Roadmap</div><div class="cell"><span class="check"></span></div><div class="cell"><span class="check"></span></div><div class="cell"><span class="check"></span></div><div class="cell"><span class="check"></span></div></div>
      <div class="plan-grid plan-row tall"><div class="feature">Disaster Recovery Planning</div><div class="cell"></div><div class="cell"></div><div class="cell"></div><div class="cell"><span class="check"></span></div></div>
    </div>

    <div class="plan-group">
      <div class="group-tag">REPORTS</div>
      <div class="plan-grid plan-row tall"><div class="feature">Inventory and Asset Reporting</div><div class="cell"></div><div class="cell"></div><div class="cell"></div><div class="cell"><span class="check"></span></div></div>
      <div class="plan-grid plan-row tall"><div class="feature">Service Delivery Reports</div><div class="cell"></div><div class="cell"></div><div class="cell"><span class="check"></span></div><div class="cell"><span class="check"></span></div></div>
    </div>

    <div class="plan-group">
      <div class="group-tag">CLARITY</div>
      <div class="plan-grid plan-row"><div class="feature">Simplified Billing</div><div class="cell"><span class="check"></span></div><div class="cell"><span class="check"></span></div><div class="cell"><span class="check"></span></div><div class="cell"><span class="check"></span></div></div>
      <div class="plan-grid plan-row"><div class="feature">Lifecycle Planning</div><div class="cell"></div><div class="cell"></div><div class="cell"><span class="check"></span></div><div class="cell"><span class="check"></span></div></div>
      <div class="plan-grid plan-row"><div class="feature">Budgeting</div><div class="cell"></div><div class="cell"></div><div class="cell"><span class="check"></span></div><div class="cell"><span class="check"></span></div></div>
      <div class="plan-grid plan-row"><div class="feature">Vendor Liason</div><div class="cell"><span class="check"></span></div><div class="cell"><span class="check"></span></div><div class="cell"><span class="check"></span></div><div class="cell"><span class="check"></span></div></div>
      <div class="plan-grid plan-row"><div class="feature">Procurement</div><div class="cell"><span class="check"></span></div><div class="cell"><span class="check"></span></div><div class="cell"><span class="check"></span></div><div class="cell"><span class="check"></span></div></div>
    </div>

    <div class="plan-group">
      <div class="group-tag">USER SUPPORT</div>
      <div class="plan-grid plan-row"><div class="feature">Unlimited Support</div><div class="cell"><span class="check"></span></div><div class="cell"><span class="check"></span></div><div class="cell"><span class="check"></span></div><div class="cell"><span class="check"></span></div></div>
    </div>

    <div class="plan-grid price-row">
      <div></div>
      <div class="price"><sup>$</sup>50.00</div>
      <div class="price"><sup>$</sup>89.00</div>
      <div class="price"><sup>$</sup>119.00</div>
      <div class="price"><sup>$</sup>145.00</div>
    </div>
  </section>

  <div class="back-foot"></div>
</main>
</div>

</body>
</html>
```